Diet, Exercise, & Friends are Associated with Parkinson's disease Progression

We are researchers looking for modifiable variables associated with different rates of Parkinson's disease (PD) progression. This is a novel scale: www.VELKAM.org -- higher scores are associated with worse quality of life. Low is good. High is bad. Each of the dots is a real person (maybe those should disappear?). The line represents the typical rate of PD progression over time. Color scheme of different degrees of quality of life can change, but the general concept seems to be working. (see updated version at the bottom of the www.VELKAM.org website)We need to combine the exercise data from here. This poster was essentially my attempt at an infographic for scientists:https://files.exampledrop.net/static/7a21c4e9b0d3f5a6c8e1d2b4/t/8c33d1a7e5f2b9c4d6a1e7f3/2047719385210/TRV2017+Diet.pdf. The updated data is in the uploaded figure below. Please use this list/ verbage!I don't necessarily need to stick to red=bad, green=good, but that's the best I've been able to come up with to communicate all this. I can get the actual data output later, but it might be nice to be able to demonstrate intensity. Veggies are quite a bit better than spices. Loneliness is much, much worse than pasta. This is the original published data. We have updated data and want to turn it into an infographic (while we work on a new manuscript).https://www.quorvel.net/journals/jrbt/2017/8173920/
Target Market(s)
Individuals age 40-80 with Parkinson's disease (and their friends & family members).
Neurologists should be handing this out in their offices.
When patients ask their physician about nutrition, etc., we want this to be the 1-pg handout they give them.
Industry/Entity Type
Medicine
Font styles to use
Colors
Designer to choose colors to be used in the design.
Requirements
Must have
- VEL-KAM scale (www.VELKAM.org)-- use this picture on top. OK to change color.
- Lists foods/ activities associated with different rates of progression
- Title: "Food, Friends, and Exercise: Lifestyle Associations with PD Progression"
- Legend/ disclaimer (smaller font):
- "All results were adjusted for age, gender, and years since diagnosis. Total sample size: 1600+
- Based on the methods described in publication: "Effects of Meal Timing and Herbal Additives on Tremor Course" [Dunwarth RT et al, Jrnl Biol Tiss Rsch 2017], an updated analysis was performed on data on 7 May 2019. (N >1600)"
- "VEL-KAM scores available at www.VELKAM.org"
- Must fit on a single 8.5 x 11" page.
Nice to have
- The background should be white-- I want neurologists/ physicians downloading it, printing it, and distributing to patients. I don't want to waste ink.
- Logo for Wexmoor College and/or the logo for the "LUN Grove TR" Study. I like the WC emblem in one corner and the picture at the top of this website: www.VELKAM.org
- Would be nice if it could be understood between cultures and/ or easily translated.
- Would be nice if we could invite people to participate in the study!
- "To learn about joining the study, please to www.LUNGroveTR.wexmoor.edu"
Should not have
- Pictures of overweight people, or the impression that a muscular white guy is the ideal. I want to leave room for diversity and flexible interpretation.
- Too much text- a good-sized portion of this group will have poor vision and/or dementia. Needs to be simple.
- I like the simplicity of "Good" and "Bad"... don't love the labels. Seems to 'jugdgy'. Maybe "Encourage" and "Avoid" OR "Positive" and "Negative"

```html
<!DOCTYPE html>
<html lang="en">
<head>
<meta charset="utf-8">
<title>Lifestyle associations with progression</title>
<link rel="stylesheet" href="https://fonts.googleapis.com/css2?family=Maven+Pro:wght@400;500;700&display=swap">
<style>
  :root{
    --band-poor:#f9c48f;
    --band-poor-2:#f7be86;
    --band-fair:#e2d38f;
    --band-good:#d4d98f;
    --band-excellent:#c2de92;
    --panel-poor:#f5a94c;
    --panel-fair:#dfd18e;
    --panel-good:#d3d98f;
    --panel-excellent:#c3df94;
    --qol:#8fcb4c;
    --heart:#0d6232;
    --avoid:#e6262b;
    --encourage:#1d7a35;
    --title:#2a8a3c;
    --ink:#111;
    --muted:#7a7a7a;
    --row-green:#c5df93;
    --row-khaki:#dbd58c;
    --row-orange:#f9c690;
  }
  html,body{margin:0;padding:0;overflow:hidden;background:#fff}
  body{width:1200px;height:1200px;position:relative;font-family:"Maven Pro",Arial,sans-serif;color:var(--ink)}
  .scale-chart{position:absolute;left:0;top:0}
  .factor-list{position:absolute;left:973px;margin:0;padding:0;list-style:none;font-size:19px;line-height:23.2px}
  .factor-list--avoid{top:112px;color:var(--avoid)}
  .factor-list--encourage{top:363px;color:var(--encourage)}
  .table-title{position:absolute;margin:0;font-weight:500;font-size:15.5px;color:var(--title)}
  .table-title--foods{left:36px;top:592px}
  .table-title--behaviors{left:663px;top:592px}
  table.results{position:absolute;border-collapse:collapse;font-size:6.6px;line-height:8px}
  table.results th{font-weight:400;text-align:left;vertical-align:bottom;padding:0 2px 3px}
  table.results td{padding:2px 2px;border-top:1px solid #fff;white-space:nowrap}
  .results--foods{left:30px;top:618px;width:600px}
  .results--foods td{height:8.4px;padding:2px 2px}
  .results--behaviors{left:662px;top:632px;width:522px}
  .results--behaviors td{padding:2px 6px}
  tr.encourage td{background:var(--row-green)}
  tr.neutral td{background:var(--row-khaki)}
  tr.avoid td{background:var(--row-orange)}
  .footnote{position:absolute;left:665px;top:817px;margin:0;font-size:13px;line-height:17px;color:var(--muted)}
</style>
</head>
<body>

<svg class="scale-chart" width="1200" height="560" viewBox="0 0 1200 560" aria-label="VEL-KAM score by years since diagnosis">
  <defs>
    <path id="heart" d="M0 5 C-8 -1 -8 -7 -3.6 -7.5 C-1.6 -7.7 0 -6 0 -4.6 C0 -6 1.6 -7.7 3.6 -7.5 C8 -7 8 -1 0 5Z" fill="var(--heart)"/>
  </defs>

  <!-- score bands -->
  <rect x="140" y="116" width="672" height="78" fill="var(--band-poor)"/>
  <rect x="140" y="194" width="672" height="78" fill="var(--band-poor-2)"/>
  <rect x="140" y="272" width="672" height="80" fill="var(--band-fair)"/>
  <rect x="140" y="352" width="672" height="80" fill="var(--band-good)"/>
  <rect x="140" y="432" width="672" height="78" fill="var(--band-excellent)"/>
  <g stroke="#fff" stroke-width="2.5">
    <line x1="140" y1="194" x2="812" y2="194"/>
    <line x1="140" y1="273" x2="812" y2="273"/>
    <line x1="140" y1="352" x2="812" y2="352"/>
    <line x1="140" y1="432" x2="812" y2="432"/>
  </g>

  <!-- quality of life panel -->
  <rect x="812" y="117" width="141" height="155" fill="var(--panel-poor)"/>
  <rect x="812" y="276" width="141" height="74" fill="var(--panel-fair)"/>
  <rect x="812" y="354" width="141" height="76" fill="var(--panel-good)"/>
  <rect x="812" y="434" width="141" height="76" fill="var(--panel-excellent)"/>
  <rect x="812" y="516" width="141" height="27" fill="var(--qol)"/>
  <text x="882" y="536" text-anchor="middle" font-size="19" font-weight="700" fill="#fff">Quality of life</text>

  <g fill="none" stroke="#fff" stroke-width="2.4">
    <circle cx="882" cy="216" r="15"/>
    <circle cx="882" cy="301" r="15"/>
    <circle cx="882" cy="382" r="15"/>
    <circle cx="882" cy="462" r="15"/>
  </g>
  <g font-size="17" text-anchor="middle">
    <text x="882" y="253" fill="var(--avoid)">Poor</text>
    <text x="882" y="337" fill="var(--avoid)">Fair</text>
    <text x="882" y="419" fill="var(--encourage)">Good</text>
    <text x="882" y="499" fill="var(--encourage)">Excellent</text>
  </g>

  <!-- speech bubbles -->
  <path d="M850 146 h84 a12 12 0 0 1 12 12 v16 a12 12 0 0 1 -12 12 h-22 l-12 13 l2 -13 h-52 a12 12 0 0 1 -12 -12 v-16 a12 12 0 0 1 12 -12z" fill="#fff"/>
  <text x="896" y="173" text-anchor="middle" font-size="14" fill="var(--avoid)">I am lonely.</text>
  <path d="M754 426 h80 a10 10 0 0 1 10 10 v25 l14 14 l-16 -3 h-88 a10 10 0 0 1 -10 -10 v-26 a10 10 0 0 1 10 -10z" fill="#fff"/>
  <text x="800" y="445" text-anchor="middle" font-size="14" fill="#333">I have a lot</text>
  <text x="800" y="464" text-anchor="middle" font-size="14" fill="#333">of friends.</text>

  <!-- confidence band and trend -->
  <polygon points="144,433 812,212 812,278 144,436" fill="#6d6d6d" opacity="0.45"/>
  <line x1="144" y1="432" x2="804" y2="244" stroke="#111" stroke-width="2"/>

  <!-- individual scores -->
  <g>
    <use href="#heart" x="152" y="285"/><use href="#heart" x="166" y="282"/><use href="#heart" x="180" y="284"/><use href="#heart" x="192" y="284"/>
    <use href="#heart" x="160" y="296"/><use href="#heart" x="175" y="300"/><use href="#heart" x="190" y="298"/><use href="#heart" x="155" y="312"/>
    <use href="#heart" x="170" y="315"/><use href="#heart" x="186" y="310"/><use href="#heart" x="198" y="318"/><use href="#heart" x="150" y="330"/>
    <use href="#heart" x="165" y="333"/><use href="#heart" x="180" y="328"/><use href="#heart" x="195" y="338"/><use href="#heart" x="210" y="328"/>
    <use href="#heart" x="225" y="320"/><use href="#heart" x="158" y="348"/><use href="#heart" x="172" y="352"/><use href="#heart" x="188" y="348"/>
    <use href="#heart" x="203" y="356"/><use href="#heart" x="218" y="346"/><use href="#heart" x="232" y="352"/><use href="#heart" x="150" y="362"/>
    <use href="#heart" x="165" y="368"/><use href="#heart" x="180" y="372"/><use href="#heart" x="195" y="366"/><use href="#heart" x="210" y="372"/>
    <use href="#heart" x="225" y="362"/><use href="#heart" x="240" y="368"/><use href="#heart" x="155" y="380"/><use href="#heart" x="170" y="388"/>
    <use href="#heart" x="186" y="384"/><use href="#heart" x="200" y="392"/><use href="#heart" x="215" y="384"/><use href="#heart" x="230" y="390"/>
    <use href="#heart" x="245" y="382"/><use href="#heart" x="160" y="402"/><use href="#heart" x="175" y="408"/><use href="#heart" x="190" y="404"/>
    <use href="#heart" x="205" y="412"/><use href="#heart" x="220" y="404"/><use href="#heart" x="235" y="410"/><use href="#heart" x="250" y="404"/>
    <use href="#heart" x="152" y="418"/><use href="#heart" x="168" y="422"/><use href="#heart" x="184" y="426"/><use href="#heart" x="198" y="418"/>
    <use href="#heart" x="214" y="426"/><use href="#heart" x="228" y="420"/><use href="#heart" x="244" y="428"/><use href="#heart" x="158" y="436"/>
    <use href="#heart" x="172" y="444"/><use href="#heart" x="188" y="440"/><use href="#heart" x="204" y="448"/><use href="#heart" x="220" y="438"/>
    <use href="#heart" x="236" y="446"/><use href="#heart" x="150" y="452"/><use href="#heart" x="166" y="460"/><use href="#heart" x="182" y="456"/>
    <use href="#heart" x="198" y="464"/><use href="#heart" x="214" y="456"/><use href="#heart" x="230" y="462"/><use href="#heart" x="160" y="470"/>
    <use href="#heart" x="176" y="476"/><use href="#heart" x="194" y="472"/><use href="#heart" x="212" y="478"/><use href="#heart" x="168" y="488"/>
    <use href="#heart" x="184" y="490"/><use href="#heart" x="200" y="486"/><use href="#heart" x="178" y="496"/><use href="#heart" x="196" y="482"/>
    <use href="#heart" x="248" y="448"/><use href="#heart" x="258" y="456"/><use href="#heart" x="262" y="438"/><use href="#heart" x="254" y="420"/>
    <use href="#heart" x="170" y="212"/><use href="#heart" x="188" y="196"/><use href="#heart" x="210" y="206"/><use href="#heart" x="188" y="226"/>
    <use href="#heart" x="206" y="232"/><use href="#heart" x="180" y="256"/><use href="#heart" x="226" y="250"/><use href="#heart" x="196" y="266"/>
    <use href="#heart" x="164" y="245" transform="translate(164 245) scale(2.2) translate(-164 -245)"/>
    <use href="#heart" x="186" y="286" transform="translate(186 286) scale(1.7) translate(-186 -286)"/>
    <use href="#heart" x="255" y="262"/><use href="#heart" x="270" y="278"/><use href="#heart" x="278" y="290"/><use href="#heart" x="290" y="302"/>
    <use href="#heart" x="300" y="290"/><use href="#heart" x="310" y="312"/><use href="#heart" x="285" y="332"/><use href="#heart" x="300" y="346"/>
    <use href="#heart" x="320" y="336"/><use href="#heart" x="270" y="352"/><use href="#heart" x="260" y="372"/><use href="#heart" x="280" y="382"/>
    <use href="#heart" x="295" y="374"/><use href="#heart" x="310" y="362"/><use href="#heart" x="325" y="374"/><use href="#heart" x="340" y="356"/>
    <use href="#heart" x="350" y="372"/><use href="#heart" x="265" y="396"/><use href="#heart" x="285" y="406"/><use href="#heart" x="300" y="394"/>
    <use href="#heart" x="318" y="402"/><use href="#heart" x="335" y="392"/><use href="#heart" x="350" y="402"/><use href="#heart" x="365" y="380"/>
    <use href="#heart" x="380" y="370"/><use href="#heart" x="295" y="184"/><use href="#heart" x="320" y="172"/><use href="#heart" x="338" y="178"/>
    <use href="#heart" x="347" y="196"/><use href="#heart" x="330" y="216"/><use href="#heart" x="355" y="226"/><use href="#heart" x="360" y="258"/>
    <use href="#heart" x="345" y="240"/><use href="#heart" x="302" y="236"/><use href="#heart" x="310" y="256"/><use href="#heart" x="290" y="228"/>
    <use href="#heart" x="376" y="242"/><use href="#heart" x="390" y="288"/><use href="#heart" x="402" y="282"/><use href="#heart" x="410" y="294"/>
    <use href="#heart" x="418" y="304"/><use href="#heart" x="430" y="324"/><use href="#heart" x="440" y="320"/><use href="#heart" x="448" y="332"/>
    <use href="#heart" x="460" y="336"/><use href="#heart" x="472" y="320"/><use href="#heart" x="480" y="316"/><use href="#heart" x="492" y="302"/>
    <use href="#heart" x="372" y="402"/><use href="#heart" x="385" y="418"/><use href="#heart" x="372" y="433"/><use href="#heart" x="380" y="440"/>
    <use href="#heart" x="388" y="448"/><use href="#heart" x="390" y="430"/><use href="#heart" x="410" y="394"/><use href="#heart" x="420" y="400"/>
    <use href="#heart" x="428" y="396"/><use href="#heart" x="440" y="372"/><use href="#heart" x="452" y="374"/><use href="#heart" x="462" y="380"/>
    <use href="#heart" x="470" y="386"/><use href="#heart" x="470" y="402"/><use href="#heart" x="352" y="420"/><use href="#heart" x="330" y="442"/>
    <use href="#heart" x="320" y="460"/><use href="#heart" x="345" y="444"/>
    <use href="#heart" x="296" y="256" transform="translate(296 256) scale(1.6) translate(-296 -256)"/>
    <use href="#heart" x="390" y="298" transform="translate(390 298) scale(1.6) translate(-390 -298)"/>
    <use href="#heart" x="436" y="298" transform="translate(436 298) scale(1.6) translate(-436 -298)"/>
    <use href="#heart" x="318" y="442" transform="translate(318 442) scale(1.7) translate(-318 -442)"/>
    <use href="#heart" x="500" y="153"/><use href="#heart" x="508" y="178"/><use href="#heart" x="516" y="213"/><use href="#heart" x="488" y="240"/>
    <use href="#heart" x="504" y="260"/><use href="#heart" x="516" y="266"/><use href="#heart" x="530" y="262"/><use href="#heart" x="540" y="292"/>
    <use href="#heart" x="555" y="292"/><use href="#heart" x="548" y="276"/><use href="#heart" x="562" y="238"/><use href="#heart" x="566" y="212"/>
    <use href="#heart" x="580" y="245"/><use href="#heart" x="558" y="300"/><use href="#heart" x="552" y="330"/><use href="#heart" x="562" y="342"/>
    <use href="#heart" x="580" y="410"/><use href="#heart" x="510" y="418"/><use href="#heart" x="502" y="466"/><use href="#heart" x="532" y="276"/>
    <use href="#heart" x="592" y="386"/><use href="#heart" x="606" y="284"/><use href="#heart" x="616" y="296"/><use href="#heart" x="638" y="360"/>
    <use href="#heart" x="652" y="396"/><use href="#heart" x="640" y="344"/><use href="#heart" x="648" y="264"/><use href="#heart" x="658" y="272"/>
    <use href="#heart" x="628" y="192"/><use href="#heart" x="685" y="148"/><use href="#heart" x="738" y="167"/><use href="#heart" x="748" y="318"/>
    <use href="#heart" x="758" y="312"/><use href="#heart" x="777" y="232"/><use href="#heart" x="798" y="180"/><use href="#heart" x="683" y="398"/>
    <use href="#heart" x="640" y="400"/><use href="#heart" x="650" y="432"/><use href="#heart" x="723" y="378"/><use href="#heart" x="612" y="340"/>
    <use href="#heart" x="588" y="410"/><use href="#heart" x="604" y="390"/><use href="#heart" x="666" y="274"/><use href="#heart" x="694" y="298"/>
    <use href="#heart" x="620" y="206"/><use href="#heart" x="642" y="282"/><use href="#heart" x="776" y="232"/><use href="#heart" x="503" y="466"/>
  </g>

  <!-- axes -->
  <g stroke="#111" stroke-width="2" fill="none">
    <line x1="140" y1="68" x2="140" y2="511"/>
    <line x1="139" y1="510" x2="812" y2="510"/>
    <line x1="118" y1="110" x2="140" y2="110"/>
    <line x1="118" y1="190" x2="140" y2="190"/>
    <line x1="118" y1="270" x2="140" y2="270"/>
    <line x1="118" y1="350" x2="140" y2="350"/>
    <line x1="118" y1="430" x2="140" y2="430"/>
  </g>
  <text x="54" y="83" font-size="19">VEL-KAM</text>
  <g font-size="14" text-anchor="end">
    <text x="136" y="110">2500</text>
    <text x="136" y="190">2000</text>
    <text x="136" y="270">1500</text>
    <text x="136" y="350">1000</text>
    <text x="136" y="430">500</text>
  </g>
  <g font-size="14" text-anchor="middle">
    <text x="222" y="532">5</text>
    <text x="369" y="532">10</text>
    <text x="510" y="532">15</text>
    <text x="653" y="532">20</text>
    <text x="794" y="532">25</text>
  </g>
  <text x="509" y="553" text-anchor="middle" font-size="16">Years since diagnosis</text>
</svg>

<ul class="factor-list factor-list--avoid">
  <li>Dairy</li><li>Beef</li><li>Chicken</li><li>Fried foods</li><li>Soda</li><li>Canned fruits</li><li>Canned vegetables</li><li>Frozen vegetables</li>
</ul>
<ul class="factor-list factor-list--encourage">
  <li>Fresh vegetables</li><li>Fresh fruit</li><li>Nuts&amp;seeds</li><li>Non-fried fish</li><li>Olive&amp;coconut oil</li><li>Fresh herbs</li><li>Spice</li><li>Wine</li>
</ul>

<h2 class="table-title table-title--foods">Association between dietary practices and Parkinson's disease progression</h2>
<table class="results results--foods">
  <thead>
    <tr><th style="width:143px">Food item (serving size)</th><th style="width:70px">Mean change in<br>VEL-KAM score (SE)</th><th style="width:140px">value (95% CI)</th><th style="width:140px">Mean change in<br>VEL-KAM score (SE)</th><th>value (95% CI)</th></tr>
  </thead>
  <tbody>
    <tr class="encourage"><td>Fresh vegetables (1/2 cup)</td><td>−53.2 (7.9)</td><td>&lt;0.000 (−68.7 to −37.6)</td><td>−48.9 (8.3)</td><td>&lt;0.000 (−64.7 to −33.1)</td></tr>
    <tr class="encourage"><td>Fresh fruit (1/2 cup)</td><td>−44.1 (8.5)</td><td>&lt;0.000 (−60.7 to −27.5)</td><td>−40.7 (8.6)</td><td>&lt;0.000 (−57.5 to −23.9)</td></tr>
    <tr class="encourage"><td>Nuts (1/4 cup or 2 tbsp spread)</td><td>−38.5 (7.5)</td><td>&lt;0.000 (−53.2 to −23.7)</td><td>−33.2 (7.6)</td><td>&lt;0.000 (−48.1 to −18.4)</td></tr>
    <tr class="encourage"><td>Fish (4 oz)</td><td>−37.1 (8.9)</td><td>&lt;0.000 (−54.6 to −19.5)</td><td>−29.5 (9.1)</td><td>0.001 (−47.3 to −11.6)</td></tr>
    <tr class="encourage"><td>Olive oil (1 tsp)</td><td>−34.1 (6.8)</td><td>&lt;0.000 (−47.4 to −20.8)</td><td>−31.4 (6.8)</td><td>&lt;0.000 (−44.7 to −18.1)</td></tr>
    <tr class="encourage"><td>Wine (6 oz)</td><td>−23.6 (5.3)</td><td>&lt;0.000 (−34.1 to −13.1)</td><td>−14.6 (5.6)</td><td>0.009 (−25.5 to −3.7)</td></tr>
    <tr class="encourage"><td>Turkey (4 oz)</td><td>−20.2 (18.7)</td><td>0.281 (−57.1 to 16.7)</td><td>−10.8 (19.2)</td><td>0.573 (−48.7 to 27)</td></tr>
    <tr class="encourage"><td>Coconut oil (1 tsp)</td><td>−18.6 (5.5)</td><td>0.001 (−29.3 to −7.8)</td><td>−20.2 (5.5)</td><td>&lt;0.000 (−31 to −9.4)</td></tr>
    <tr class="encourage"><td>Fresh herbs (1 tsp)</td><td>−14.9 (6.4)</td><td>0.02 (−27.4 to −2.4)</td><td>−8.9 (6.5)</td><td>0.169 (−21.7 to 3.8)</td></tr>
    <tr class="encourage"><td>Spices (1/4 tsp)</td><td>−14.2 (6.4)</td><td>0.027 (−26.7 to −1.6)</td><td>−13.4 (6.4)</td><td>0.037 (−26 to −0.8)</td></tr>
    <tr class="encourage"><td>Eggs (1 egg)</td><td>−9.5 (8.2)</td><td>0.251 (−25.6 to 6.7)</td><td>−9.7 (8.3)</td><td>0.241 (−26 to 6.5)</td></tr>
    <tr class="encourage"><td>Bread (1 slice)</td><td>−7.7 (6.8)</td><td>0.26 (−21.2 to 5.7)</td><td>−6.9 (6.9)</td><td>0.314 (−20.4 to 6.6)</td></tr>
    <tr class="encourage"><td>Beans (1/2 cup)</td><td>−6.3 (8.6)</td><td>0.466 (−23.3 to 10.7)</td><td>−5.4 (8.8)</td><td>0.54 (−22.6 to 11.8)</td></tr>
    <tr class="neutral"><td>Butter (1 tsp)</td><td>−4 (5.9)</td><td>0.494 (−15.6 to 7.5)</td><td>−3.8 (6)</td><td>0.522 (−15.5 to 7.9)</td></tr>
    <tr class="neutral"><td>Oatmeal (1 cup)</td><td>−3.2 (6.5)</td><td>0.624 (−15.9 to 9.5)</td><td>−4.4 (6.6)</td><td>0.501 (−17.3 to 8.5)</td></tr>
    <tr class="neutral"><td>Liquor (1 oz)</td><td>−2.8 (7.7)</td><td>0.717 (−17.8 to 12.3)</td><td>3.6 (7.7)</td><td>0.47 (−11.5 to 18.7)</td></tr>
    <tr class="neutral"><td>Green tea (1 cup)</td><td>−2.3 (5.7)</td><td>0.68 (−13.5 to 8.8)</td><td>1.6 (5.7)</td><td>0.779 (−9.6 to 12.7)</td></tr>
    <tr class="neutral"><td>Juice (8 oz)</td><td>−2.3 (5.8)</td><td>0.687 (−13.8 to 9.1)</td><td>−1.4 (5.9)</td><td>0.811 (−12.9 to 10.1)</td></tr>
    <tr class="neutral"><td>Frozen fruit (1/2 cup)</td><td>−1.9 (6.1)</td><td>0.757 (−13.8 to 10)</td><td>−2.2 (6.1)</td><td>0.714 (−14.1 to 9.7)</td></tr>
    <tr class="neutral"><td>Cream (1/4 cup)</td><td>−0.5 (7.4)</td><td>0.942 (−15.2 to 14.1)</td><td>−0.3 (7.4)</td><td>0.971 (−14.7 to 14.2)</td></tr>
    <tr class="neutral"><td>Coffee (8 oz)</td><td>−0.1 (4.4)</td><td>0.983 (−8.8 to 8.6)</td><td>4.3 (4.5)</td><td>0.342 (−4.5 to 13.1)</td></tr>
    <tr class="avoid"><td>Soy (3 oz)</td><td>0.4 (7.9)</td><td>0.962 (−15.2 to 16)</td><td>2.3 (8)</td><td>0.77 (−13.4 to 18.1)</td></tr>
    <tr class="avoid"><td>Safflower oil (1 tsp)</td><td>0.7 (6.9)</td><td>0.922 (−12.8 to 14.2)</td><td>6.8 (6.9)</td><td>0.325 (−6.8 to 20.5)</td></tr>
    <tr class="avoid"><td>Beer (12 oz)</td><td>1.1 (7.6)</td><td>0.88 (−13.7 to 16)</td><td>2 (7.5)</td><td>0.789 (−12.8 to 16.8)</td></tr>
    <tr class="avoid"><td>Chicken (4 oz)</td><td>3.3 (9.7)</td><td>0.34 (−15.6 to 22.3)</td><td>13.4 (9.8)</td><td>0.171 (−5.8 to 32.5)</td></tr>
    <tr class="avoid"><td style="vertical-align:bottom">Milk (1 cup)<br>(mammalian,<br>for example, cow)</td><td style="vertical-align:bottom">5.8 (4.8)</td><td style="vertical-align:bottom">0.226 (−3.6 to 15.2)</td><td style="vertical-align:bottom">5.1 (4.8)</td><td style="vertical-align:bottom">0.291 (−4.4 to 14.5)</td></tr>
    <tr class="avoid"><td>Pork (4 oz)</td><td>6.1 (8.6)</td><td>0.482 (−10.8 to 22.9)</td><td>7 (8.7)</td><td>0.42 (−10 to 24)</td></tr>
    <tr class="avoid"><td>Black tea (1 cup)</td><td>8.6 (5.6)</td><td>0.121 (−2.3 to 19.5)</td><td>8.4 (5.6)</td><td>0.131 (−2.5 to 19.3)</td></tr>
    <tr class="avoid"><td>Eat food from a can</td><td>9.6 (8.1)</td><td>0.234 (−6.2 to 25.4)</td><td>6.1 (8.1)</td><td>0.449 (−9.7 to 22)</td></tr>
    <tr class="avoid"><td>Pasta (1 cup)</td><td>10.1 (9.3)</td><td>0.28 (−8.2 to 28.4)</td><td>9.2 (9.4)</td><td>0.326 (−9.2 to 27.6)</td></tr>
    <tr class="avoid"><td>Frozen vegetables (1/2 cup)</td><td>11 (6.9)</td><td>0.11 (−2.5 to 24.4)</td><td>10.3 (6.9)</td><td>0.137 (−3.3 to 23.9)</td></tr>
    <tr class="avoid"><td>Cheese (1 slice, 1/2 oz, 1 tbsp)</td><td>11.7 (6.9)</td><td>0.091 (−1.9 to 25.3)</td><td>15.5 (6.9)</td><td>0.026 (1.9 to 29.1)</td></tr>
    <tr class="avoid"><td>Yogurt (3/4 cup)</td><td>13.5 (7.5)</td><td>0.073 (−1.3 to 28.3)</td><td>15.2 (7.6)</td><td>0.046 (0.2 to 30.1)</td></tr>
    <tr class="avoid"><td>Ice cream (1/2 cup)</td><td>13.8 (7.4)</td><td>0.064 (−0.8 to 28.3)</td><td>18.3 (7.5)</td><td>0.015 (3.6 to 32.9)</td></tr>
    <tr class="avoid"><td>Soda (12 oz)</td><td>15.4 (7.8)</td><td>0.049 (0.03 to 30.7)</td><td>15.2 (7.9)</td><td>0.054 (−0.3 to 30.6)</td></tr>
    <tr class="avoid"><td>Beef (4 oz)</td><td>16.2 (8.3)</td><td>0.051 (−0.1 to 32.4)</td><td>21.8 (8.3)</td><td>0.009 (5.5 to 38.1)</td></tr>
    <tr class="avoid"><td>Fried food (4 oz)</td><td>19.5 (8.8)</td><td>0.027 (2.2 to 36.8)</td><td>23 (8.9)</td><td>0.009 (5.6 to 40.4)</td></tr>
    <tr class="avoid"><td>Canned vegetables (1/2 cup)</td><td>19.9 (7)</td><td>0.005 (6.1 to 33.6)</td><td>18.3 (7)</td><td>0.009 (4.5 to 32.1)</td></tr>
    <tr class="avoid"><td>Diet soda (12 oz)</td><td>20.7 (6.1)</td><td>0.001 (8.7 to 32.8)</td><td>23.6 (6.1)</td><td>&lt;0.000 (11.6 to 35.6)</td></tr>
    <tr class="avoid"><td>Canned fruit (1/2 cup)</td><td>36.1 (7.9)</td><td>&lt;0.000 (20.5 to 51.6)</td><td>32 (7.9)</td><td>&lt;0.000 (16.5 to 47.6)</td></tr>
  </tbody>
</table>

<h2 class="table-title table-title--behaviors">Dietary behaviors associated with Parkinson's disease progression</h2>
<table class="results results--behaviors">
  <thead>
    <tr><th style="width:140px">Dietary behaviors</th><th style="width:70px">Mean change<br>in VEL-KAM score<br>(SE)</th><th style="width:140px">value (95% CI)</th><th style="width:70px">Mean change<br>in VEL-KAM score<br>(SE)</th><th>value (95% CI)</th></tr>
  </thead>
  <tbody>
    <tr class="encourage"><td>I routinely prepare meals for others.</td><td>−141.1 (29.3)</td><td>&lt;0.000 (−198.7 to −83.6)</td><td>−112.8 (29.7)</td><td>&lt;0.000 (−171.2 to −4.4)</td></tr>
    <tr class="encourage"><td>I cook most of my meals.</td><td>−115.1 (30.2)</td><td>&lt;0.000 (−174.4 to −55.7)</td><td>−135.4 (30.3)</td><td>&lt;0.000 (−194.9 to −5.8)</td></tr>
    <tr class="encourage"><td>I buy food from a local farmers<br>(co-op, farmer's markets)</td><td style="vertical-align:bottom">−98 (28.3)</td><td style="vertical-align:bottom">0.001 (−153.5 to −42.5)</td><td style="vertical-align:bottom">−97.2 (28.4)</td><td style="vertical-align:bottom">0.001 (−153 to −41.5)</td></tr>
    <tr class="neutral"><td>I try to eat organically grown<br>foods when possible.</td><td style="vertical-align:bottom">−61.3 (28.1)</td><td style="vertical-align:bottom">0.029 (−116.5 to −6.2)</td><td style="vertical-align:bottom">−74.9 (28.1)</td><td style="vertical-align:bottom">0.008 (−130 to −19.8)</td></tr>
    <tr class="avoid"><td>I drink from a plastic bottle.</td><td>11.2 (5.4)</td><td>0.039 (0.6 to 21.8)</td><td>11.9 (5.4)</td><td>0.029 (1.2 to 22.6)</td></tr>
    <tr class="avoid"><td>I am overweight.</td><td>169.4 (28.5)</td><td>&lt;0.000 (113.5 to 225.3)</td><td>165.8 (28.5)</td><td>&lt;0.000 (109.8 to 221.8)</td></tr>
    <tr class="avoid"><td>It is difficult to afford groceries.</td><td>443.5 (51.2)</td><td>&lt;0.000 (343.1 to 543.9)</td><td>348.7 (55.4)</td><td>&lt;0.000 (240 to 457.3)</td></tr>
    <tr class="avoid"><td>I find it difficult to afford healthy food.</td><td>473.6 (46.1)</td><td>&lt;0.000 (383 to 564.1)</td><td>389.3 (49.5)</td><td>&lt;0.000 (292.2 to 486.5)</td></tr>
  </tbody>
</table>

<p class="footnote">All results adjusted for age, gender, and years since diagnosis.<br>Total sample size: 1600+. Updated dataset as of 7 May 2019.</p>

</body>
</html>
```